clean web design for a recruitment company

We need a web design for a company called 'TORAVI' recruitment. We are a new age recruitment companies that selects people by their true nature, values and what they can bring to the table as a tangible talent. We are all here possessing a certain talent, whatever that could be that the world needs. The final design should communicate professionalism and strongly embedded etiquette we believe in and a branding promise 'Seeing ones true nature'. Our companies values are integrity, giving away to the community, cherishing the sharing of our talent, time and helping one another.

Target Market(s)

Gulf Countries

Industry/Entity Type

It Company

Number of Pages Required

1 page

Font styles to use
Serif

Requirements
Must have
• Clear and readable font, user friendly structure and easy navigation menus.
Nice to have
• Extra sort of ideas on images we may use, tag lines etc. sample sites we love site:https://www.velmaroque.com/
• http://www.dorisaklund.com/
• http://www.pebblemoorhouse.com/idea-gallery/
Should not have
• all sort of colors, big combination of fonts, images with people in the office or people in suits likewise all the typical industry web sites

```html
<!DOCTYPE html>
<html lang="en">
<head>
<meta charset="utf-8">
<title>Toravi Recruitment</title>
<link href="https://fonts.googleapis.com/css2?family=Open+Sans:wght@300;400;600;700&display=swap" rel="stylesheet">
<style>
:root{
  --ink:#2b2b2b;
  --text:#6f6f6f;
  --muted:#9a9a9a;
  --line:#e4e4e4;
  --black:#111;
  --footer:#1d1d1d;
  --footer-bottom:#121212;
  --footer-text:#9b9b9b;
  --white:#fff;
  --hero-a:#3a3632;
  --hero-b:#8a837a;
}
*{margin:0;padding:0;box-sizing:border-box}
html,body{width:880px;height:1200px;overflow:hidden}
body{font-family:"Open Sans",Arial,sans-serif;color:var(--text);background:var(--white);position:relative}
.wrap{position:absolute;left:82px;width:716px}

/* header */
.site-header{position:absolute;top:0;left:0;width:880px;height:140px;background:var(--white)}
.brand{position:absolute;left:82px;top:12px;display:flex;flex-direction:column;align-items:center;width:96px}
.brand-square{width:56px;height:62px;background:var(--black)}
.brand-name{margin-top:8px;font-size:24px;font-weight:400;color:var(--ink);letter-spacing:1px;line-height:1}
.contact-bar{position:absolute;right:82px;top:16px;font-size:10px;color:var(--muted);display:flex;gap:18px;align-items:center}
.contact-bar span{display:flex;align-items:center;gap:5px}
.main-nav{position:absolute;right:82px;top:74px;display:flex;gap:0;font-size:9px;font-weight:600;letter-spacing:.5px}
.main-nav a{color:var(--muted);text-decoration:none;padding:8px 13px;text-transform:uppercase}
.main-nav a.active{color:var(--ink);border-bottom:2px solid var(--ink)}

/* hero */
.hero{position:absolute;top:140px;left:0;width:880px;height:323px;background:linear-gradient(100deg,var(--hero-a),var(--hero-b) 45%,var(--hero-a));}
.hero-caption{position:absolute;left:0;bottom:0;width:880px;height:88px;background:rgba(20,18,16,.55)}
.hero-title{position:absolute;left:108px;top:18px;font-size:28px;font-weight:400;color:var(--white);letter-spacing:1px}
.hero-dots{position:absolute;left:110px;top:62px;display:flex;gap:6px}
.hero-dots i{width:12px;height:12px;border-radius:50%;background:rgba(255,255,255,.85);display:block}

/* sections */
.section-title{text-align:center;font-size:15px;font-weight:600;color:var(--ink);letter-spacing:.5px;text-transform:uppercase}
.section-text{text-align:center;font-size:9.5px;line-height:1.6;margin-top:10px}
.welcome{top:486px}
.method{top:580px}
.divider{position:absolute;left:82px;width:716px;height:1px;background:var(--line)}

.values{top:680px;display:flex;justify-content:space-between}
.value{width:160px;text-align:center}
.value svg{display:block;margin:0 auto;height:40px}
.value h3{font-size:11px;font-weight:700;color:var(--ink);text-transform:uppercase;margin-top:10px}
.value p{font-size:9px;line-height:1.55;margin-top:6px}

.team{top:868px}
.members{top:932px;display:flex;justify-content:space-between}
.member{width:220px;display:flex;gap:12px;align-items:flex-start}
.avatar{width:52px;height:52px;border-radius:50%;background:linear-gradient(135deg,#c9c5c0,#7d7873);flex:none}
.member h4{font-size:10px;font-weight:600;color:var(--ink)}
.member p{font-size:8.5px;line-height:1.5;margin-top:4px}

/* footer */
.site-footer{position:absolute;top:1027px;left:0;width:880px;height:146px;background:var(--footer)}
.footer-col{position:absolute;top:20px}
.footer-col h5{font-size:12px;font-weight:600;color:var(--white);text-transform:uppercase;padding-bottom:8px;border-bottom:1px solid #333;margin-bottom:12px}
.quick-links{left:82px;width:230px}
.link-grid{display:grid;grid-template-columns:repeat(3,1fr);row-gap:7px;font-size:8.5px;color:var(--footer-text)}
.newsletter{left:370px;width:210px}
.signup{display:flex;margin-top:4px}
.signup .field{width:130px;height:26px;background:var(--white);font-size:8px;color:var(--muted);padding:8px}
.signup .button{width:70px;height:26px;background:#000;color:var(--white);font-size:8px;font-weight:700;text-align:center;line-height:26px;letter-spacing:.5px}
.connect{left:626px;width:172px}
.socials{display:flex;gap:6px}
.socials i{width:22px;height:22px;background:#4a4a4a;display:block}
.footer-bottom{position:absolute;top:1173px;left:0;width:880px;height:27px;background:var(--footer-bottom);font-size:8px;color:#777}
.footer-bottom .legal{position:absolute;left:82px;top:9px}
.footer-bottom .copy{position:absolute;right:82px;top:9px}
</style>
</head>
<body>

<header class="site-header">
  <div class="brand">
    <div class="brand-square"></div>
    <div class="brand-name">toravi</div>
  </div>
  <div class="contact-bar">
    <span>
      <svg width="10" height="10" viewBox="0 0 10 10"><path d="M2 1l2 2-1 1.2c.6 1.2 1.6 2.2 2.8 2.8L7 6l2 2-1.4 1.4C4.5 9 1 5.5.6 2.4z" fill="#9a9a9a"/></svg>
      +971 50 000 0000
    </span>
    <span>
      <svg width="11" height="8" viewBox="0 0 11 8"><rect x=".5" y=".5" width="10" height="7" fill="none" stroke="#9a9a9a"/><path d="M.5.5l5 4 5-4" fill="none" stroke="#9a9a9a"/></svg>
      info@toravi-mena.com
    </span>
  </div>
  <nav class="main-nav">
    <a class="active" href="#">Home</a>
    <a href="#">Team</a>
    <a href="#">Methodology</a>
    <a href="#">Specialist Areas</a>
    <a href="#">Clients</a>
    <a href="#">Candidates</a>
    <a href="#">Toravi Group</a>
  </nav>
</header>

<section class="hero" role="img" aria-label="Gallery wall of framed black and white portrait photographs">
  <div class="hero-caption">
    <h1 class="hero-title">SEEING ONES TRUE NATURE</h1>
    <div class="hero-dots"><i></i><i></i></div>
  </div>
</section>

<section class="wrap welcome">
  <h2 class="section-title">Welcome to Toravi</h2>
  <p class="section-text">Toravi is a recruitment partner for technology teams across the Gulf. We look past the résumé to the person behind it, their values, their character and the talent they bring to the table. Every placement begins with a conversation, not a checklist, so that the people we introduce fit the culture as well as the role. We stay close to clients and candidates long after the first day.</p>
</section>

<div class="divider" style="top:568px"></div>

<section class="wrap method">
  <h2 class="section-title">Methodology</h2>
  <p class="section-text">Our method rests on four simple ideas that guide every search we run. We listen first, we look for true nature, we join the threads between people and we follow a model built on trust and shared values.</p>
</section>

<section class="wrap values">
  <div class="value">
    <svg viewBox="0 0 60 40" width="60"><path d="M4 20l12-10 10 4 8-4 12 2 10 8-14 12-8-6-8 6z" fill="#333"/></svg>
    <h3>We Believe</h3>
    <p>Integrity shapes each step. We speak openly with clients and candidates and keep every promise we make along the way.</p>
  </div>
  <div class="value">
    <svg viewBox="0 0 40 40" width="40"><circle cx="20" cy="14" r="12" fill="#333"/><rect x="18" y="22" width="4" height="16" fill="#333"/></svg>
    <h3>True Nature</h3>
    <p>We look for the talent a person was born with and the values they live by every working day.</p>
  </div>
  <div class="value">
    <svg viewBox="0 0 50 40" width="50"><circle cx="10" cy="8" r="5" fill="#333"/><circle cx="25" cy="8" r="5" fill="#333"/><circle cx="40" cy="8" r="5" fill="#333"/><rect x="6" y="15" width="8" height="18" fill="#333"/><rect x="21" y="15" width="8" height="18" fill="#333"/><rect x="36" y="15" width="8" height="18" fill="#333"/><path d="M2 26h46" stroke="#333" stroke-width="2"/></svg>
    <h3>Micro Thread</h3>
    <p>We weave people, teams and goals together, finding the links that make a placement last for years.</p>
  </div>
  <div class="value">
    <svg viewBox="0 0 56 40" width="56"><circle cx="28" cy="9" r="6" fill="#333"/><circle cx="12" cy="13" r="5" fill="#333"/><circle cx="44" cy="13" r="5" fill="#333"/><path d="M18 36c0-12 20-12 20 0z" fill="#333"/><path d="M3 36c0-10 16-10 16 0zM37 36c0-10 16-10 16 0z" fill="#333"/></svg>
    <h3>Toravi The Model</h3>
    <p>A clear process from first call to final offer, shared with you at every stage of the search.</p>
  </div>
</section>

<section class="wrap team">
  <h2 class="section-title">Our Team</h2>
  <p class="section-text">A small team of consultants who know the Gulf technology market and care about the people in it.</p>
</section>

<section class="wrap members">
  <div class="member">
    <div class="avatar" role="img" aria-label="Portrait of team member"></div>
    <div><h4>Sami Haddad</h4><p>Senior consultant with ten years of experience placing engineers across the region.</p></div>
  </div>
  <div class="member">
    <div class="avatar" role="img" aria-label="Portrait of team member"></div>
    <div><h4>Laila Noor</h4><p>Senior consultant with ten years of experience placing engineers across the region.</p></div>
  </div>
  <div class="member">
    <div class="avatar" role="img" aria-label="Portrait of team member"></div>
    <div><h4>Omar Fadel</h4><p>Senior consultant with ten years of experience placing engineers across the region.</p></div>
  </div>
</section>

<footer class="site-footer">
  <div class="footer-col quick-links">
    <h5>Quick Links</h5>
    <div class="link-grid">
      <span>Home</span><span>Specialist Areas</span><span>Toravi Group</span>
      <span>Team</span><span>Clients</span><span>Contact Us</span>
      <span>Methodology</span><span>Candidates</span><span>FAQs</span>
    </div>
  </div>
  <div class="footer-col newsletter">
    <h5>Newsletter Signup</h5>
    <div class="signup"><div class="field">Email address</div><div class="button">SUBSCRIBE</div></div>
  </div>
  <div class="footer-col connect">
    <h5>Connect Us</h5>
    <div class="socials"><i></i><i></i><i></i><i></i><i></i><i></i></div>
  </div>
</footer>
<div class="footer-bottom">
  <span class="legal">Privacy Policy &nbsp;|&nbsp; Sitemap</span>
  <span class="copy">Copyright © 2014 Toravi. All rights reserved</span>
</div>

</body>
</html>
```